【依頼の目的/概要】
電子書籍(plumet)の表紙デザインをお願いします。

【画像サイズ】
表紙ファイルの理想的な寸法は2,560×1,600ピクセルです。

【タイトル】
あの窓辺にまた灯りがともる静かな暮らしの場を一から育てるための手引き

サブキャッチ
~住む人の歩みを一緒に編み直す語らい中心の新しい手法~

【著者】
株式会社MRTOV
代表取締役 江坂 なつえ

【本の内容】
誰もが迎える老いのステージを「自分の人生まんざらでもなかったなぁ」と思っていただける新手法ナラティブアプローチの方法を介護哲学と共に解説しています。

*本文を参考資料として添付します。

【デザイン要望】
特にイメージにこだわりはありませんので、自由な発想でのデザインご応募を楽しみにしています。
*次点、次次点の方への参加報酬を設定いたしました。
*その他、必要な情報がありましたらお問い合わせください。

暖かいイメージが伝わってきます。
一番人気でした。

この度は力作を多数ご提案いただき、有難うございました。
初めてワクトリアを利用させていただいたのですが、たくさんの洗練されたご提案があったこと、はるかに自分の予想を上回りました。
これからも、利用させていただきたいと思いますので、よろしくお願いいたします。

```html
<!DOCTYPE html>
<html lang="ja">
<head>
<meta charset="utf-8">
<title>あの窓辺にまた灯りがともる静かな暮らしの場を一から育てるための手引き</title>
<link href="https://fonts.googleapis.com/css2?family=Noto+Sans+JP:wght@500;700;900&family=Cormorant+Garamond:wght@400&display=swap" rel="stylesheet">
<style>
  :root {
    --bg: #a8b8e6;
    --panel: #ffffff;
    --ink: #1d2340;
    --highlight: #ffe94a;
    --ghost: rgba(255, 255, 255, 0.55);
    --art-a: #c3cff1;
    --art-b: #98aadf;
  }
  * { margin: 0; padding: 0; box-sizing: border-box; }
  html, body { width: 750px; height: 1200px; overflow: hidden; background: var(--bg); }
  .cover {
    position: relative;
    width: 750px;
    height: 1200px;
    background: var(--bg);
    font-family: "Noto Sans JP", sans-serif;
    color: var(--ink);
    overflow: hidden;
  }
  .title-panel {
    position: absolute;
    left: 75px; top: 80px;
    width: 655px; height: 245px;
    background: var(--panel);
    border-radius: 22px;
    display: flex; align-items: center; justify-content: center;
  }
  .title {
    font-weight: 900;
    font-size: 40px;
    line-height: 1.45;
    letter-spacing: 0.02em;
    white-space: nowrap;
  }
  .title span { display: block; }
  .subtitle-line {
    position: absolute;
    left: 92px;
    font-weight: 700;
    font-size: 36px;
    line-height: 1.3;
    white-space: nowrap;
    letter-spacing: 0.01em;
  }
  .subtitle-line.one { top: 375px; }
  .subtitle-line.two { top: 462px; }
  .mark { background: linear-gradient(transparent 50%, var(--highlight) 50%); }
  .subtitle-line.two .mark { background: var(--highlight); padding: 0 4px; }
  .caregiver-art {
    position: absolute;
    left: 175px; top: 545px;
    width: 510px; height: 345px;
    border-radius: 18px;
    background: linear-gradient(180deg, var(--art-a), var(--art-b));
  }
  .ghost-word {
    position: absolute;
    left: -4px;
    font-family: "Cormorant Garamond", serif;
    font-weight: 400;
    font-size: 132px;
    line-height: 1;
    color: var(--ghost);
    letter-spacing: 0.02em;
    white-space: nowrap;
  }
  .ghost-word.first { top: 905px; }
  .ghost-word.second { top: 1040px; }
  .author {
    position: absolute;
    left: 420px; top: 900px;
    font-weight: 700;
    white-space: nowrap;
    z-index: 2;
  }
  .author .company { display: block; font-size: 20px; line-height: 1.6; margin-bottom: 4px; }
  .author .role { font-size: 18px; margin-right: 8px; }
  .author .name { font-size: 32px; font-weight: 900; letter-spacing: 0.03em; }
</style>
</head>
<body>
<main class="cover">
  <div class="title-panel">
    <h1 class="title">
      <span>あの窓辺にまた灯りがともる</span>
      <span>静かな暮らしの場を一から</span>
      <span>育てるための手引き</span>
    </h1>
  </div>

  <p class="subtitle-line one">住む人の歩みを一緒に<span class="mark">編み直す</span></p>
  <p class="subtitle-line two"><span class="mark">語らい中心の新しい手法</span></p>

  <div class="caregiver-art" role="img" aria-label="Illustration of two caregivers pushing elderly residents in wheelchairs"></div>

  <div class="ghost-word first" aria-hidden="true">NARRATIVE</div>
  <div class="ghost-word second" aria-hidden="true">APROACH</div>

  <p class="author">
    <span class="company">株式会社MRTOV</span>
    <span class="role">代表取締役</span><span class="name">江坂 なつえ</span>
  </p>
</main>
</body>
</html>
```